We have developed a fully functional App called Corvalink. However, it requires a nicer GUI. You can see screenshots of our App on www.corvalink-example.com under "Tutorial". For those of you with Android, you can also install it. When you go to Corvalink-example.com, your phone will automatically redirect you to download. From there, you'll get a better idea of what our App looks like and how your design can make it way better. Please note we expect a design idea for most screens (there's about 8 screens) but do just one screen first and if you win, you can do the other 8 after.

Target Market(s)

People looking for dating / flirting

Industry/Entity Type

Android

Requirements
Must have
• sleek looking

```html
<!DOCTYPE html>
<html lang="en">
<head>
<meta charset="utf-8">
<title>Corvalink – App Screens</title>
<link rel="stylesheet" href="https://fonts.googleapis.com/css2?family=Arimo:wght@400;700&display=swap">
<style>
:root{
  --page:#ffffff;
  --header:#0f5b91;
  --header-active:#0a4a78;
  --header-line:#0d5286;
  --sky-top:#6aaede;
  --sky-mid:#8fd0ea;
  --sky-low:#a3b4d8;
  --sky-bottom:#6c7fb9;
  --white:#ffffff;
  --name:#0f5b91;
  --age:#c8106e;
  --online:#3cb518;
  --body-text:#333333;
  --field:#eeeeee;
  --field-text:#999999;
  --caret:#444444;
  --arrow:#666666;
  --silhouette:#666666;
  --tab:#a20d70;
  --tab-active:#cc1590;
  --ring-a:#c8106e;
  --ring-b:#1c5fa0;
}
*{box-sizing:border-box;margin:0;padding:0}
html,body{width:1200px;height:1038px;overflow:hidden;background:var(--page)}
body{position:relative;font-family:"Arimo",Arial,sans-serif}

.screen{position:absolute;top:49px;width:522px;height:929px;overflow:hidden;
  background:linear-gradient(180deg,var(--sky-top) 0%,var(--sky-mid) 20%,var(--sky-low) 62%,var(--sky-bottom) 100%)}
.screen--feed{left:55px}
.screen--profile{left:621px}

.app-bar{position:absolute;left:0;top:0;width:100%;height:114px;background:var(--header);display:flex}
.brand{flex:1;display:flex;align-items:center;gap:12px;padding-left:23px;color:var(--white);font-weight:700;font-size:27px}
.brand-dot{width:30px;height:30px;border-radius:50%;background:var(--white)}
.nav-tab{width:95px;height:114px;display:flex;align-items:center;justify-content:center;border-left:2px solid var(--header-line)}
.nav-tab--active{background:var(--header-active)}
.nav-tab svg{fill:var(--white)}

/* feed */
.match{position:absolute;left:0;width:100%}
.avatar{position:absolute;left:26px;width:140px;height:140px;border-radius:50%;
  background:linear-gradient(135deg,var(--ring-a),var(--ring-b));padding:4px}
.avatar-inner{width:100%;height:100%;border-radius:50%;border:5px solid var(--white)}
.location{position:absolute;left:0;width:192px;text-align:center;color:var(--white);font-size:16px}
.bubble{position:absolute;left:196px;width:296px;background:var(--white);border-radius:5px;padding:18px 20px 0 23px}
.bubble::before{content:"";position:absolute;left:-11px;top:28px;border:8px solid transparent;border-right:11px solid var(--white);border-left:0}
.bubble-name{font-size:21px;font-weight:700;color:var(--name);display:flex;align-items:center}
.bubble-name .status{width:13px;height:13px;border-radius:50%;background:var(--online);margin-right:12px}
.bubble-name .age{color:var(--age);margin-left:6px}
.bubble-text{margin-top:8px;font-size:17.5px;line-height:23px;color:var(--body-text)}

/* profile form */
.field{position:absolute;background:var(--field);border-radius:5px;color:var(--field-text);font-size:21px;display:flex;align-items:center;padding-left:23px}
.field--filled{background:var(--white);color:var(--body-text)}
.caret{display:inline-block;width:2px;height:24px;background:var(--caret);margin-left:2px}
.field .chevron{position:absolute;right:20px;top:50%;margin-top:-9px;border-left:11px solid transparent;border-right:11px solid transparent;border-top:18px solid var(--arrow)}
.pics-label{position:absolute;left:48px;top:580px;color:var(--white);font-size:21px}
.pic{position:absolute;top:624px;width:101px;height:100px;background:var(--field);border-radius:3px;display:flex;align-items:center;justify-content:center}
.pic--photo{background:linear-gradient(160deg,#4a3c3a,#d6a99a 55%,#6a4a45)}
.pic svg{fill:var(--silhouette)}

.tab-bar{position:absolute;left:0;bottom:0;width:100%;height:49px;display:flex;background:var(--tab)}
.tab-bar .tab{flex:1;color:var(--white);font-size:19px;display:flex;align-items:center;justify-content:center;position:relative}
.tab-bar .tab--active{background:var(--tab-active)}
.tab-bar .tab--active::before{content:"";position:absolute;top:-14px;left:50%;margin-left:-14px;border-left:14px solid transparent;border-right:14px solid transparent;border-bottom:14px solid var(--tab-active)}
</style>
</head>
<body>

<svg width="0" height="0" style="position:absolute">
  <defs>
    <symbol id="icon-home" viewBox="0 0 32 32"><path d="M16 3 2 15h4v14h8v-9h4v9h8V15h4z"/></symbol>
    <symbol id="icon-mail" viewBox="0 0 40 28"><path d="M1 1h38v26H1z M3 4v21h34V4L20 17z" fill-rule="evenodd"/><path d="M3 2h34L20 15z"/></symbol>
    <symbol id="icon-gear" viewBox="0 0 36 36"><path fill-rule="evenodd" d="M15 1h6l1 5 4 2 4-3 4 4-3 4 2 4 5 1v6l-5 1-2 4 3 4-4 4-4-3-4 2-1 5h-6l-1-5-4-2-4 3-4-4 3-4-2-4-5-1v-6l5-1 2-4-3-4 4-4 4 3 4-2z M18 11a7 7 0 1 0 0.01 0z M18 14a4 4 0 1 1-0.01 0z"/></symbol>
    <symbol id="icon-person" viewBox="0 0 60 60"><circle cx="30" cy="18" r="13"/><path d="M4 58c0-16 11-24 26-24s26 8 26 24z"/></symbol>
  </defs>
</svg>

<section class="screen screen--feed">
  <header class="app-bar">
    <div class="brand"><span class="brand-dot"></span>Corvalink</div>
    <div class="nav-tab nav-tab--active"><svg width="36" height="36"><use href="#icon-home"/></svg></div>
    <div class="nav-tab"><svg width="42" height="30"><use href="#icon-mail"/></svg></div>
    <div class="nav-tab"><svg width="38" height="38"><use href="#icon-gear"/></svg></div>
  </header>

  <article class="match" style="top:150px">
    <div class="avatar" style="top:1px"><div class="avatar-inner" role="img" aria-label="Profile photo of Tessa Morlane" style="background:linear-gradient(160deg,#8a8f96,#e8c2b4 55%,#b27d6e)"></div></div>
    <div class="location" style="top:154px">New York, USA</div>
    <div class="bubble" style="top:0;height:127px">
      <div class="bubble-name"><span class="status"></span>Tessa Morlane,<span class="age">28</span></div>
      <p class="bubble-text">Cool I love it, tonight should be very eventful!</p>
    </div>
  </article>

  <article class="match" style="top:364px">
    <div class="avatar" style="top:3px"><div class="avatar-inner" role="img" aria-label="Profile photo of Benny-Ben" style="background:linear-gradient(160deg,#4a4a4e,#c9b5ac 55%,#7d7f86)"></div></div>
    <div class="location" style="top:156px">Sacramento, USA</div>
    <div class="bubble" style="top:0;height:151px">
      <div class="bubble-name"><span class="status"></span>Benny-Ben,<span class="age">33</span></div>
      <p class="bubble-text">I hope this design would be chosen. If it does happen then it's cool!</p>
    </div>
  </article>

  <article class="match" style="top:572px">
    <div class="avatar" style="top:2px"><div class="avatar-inner" role="img" aria-label="Profile photo of Marisol" style="background:linear-gradient(160deg,#2e2624,#e2b9a8 55%,#5a3e3a)"></div></div>
    <div class="location" style="top:155px">Chicago, USA</div>
    <div class="bubble" style="top:0;height:150px">
      <div class="bubble-name"><span class="status"></span>Marisol,<span class="age">28</span></div>
      <p class="bubble-text">Hi benny-ben how are you. If you win you should treat me for a dinner :)</p>
    </div>
  </article>
</section>

<section class="screen screen--profile">
  <header class="app-bar">
    <div class="brand"><span class="brand-dot"></span>Corvalink</div>
    <div class="nav-tab"><svg width="36" height="36"><use href="#icon-home"/></svg></div>
    <div class="nav-tab"><svg width="42" height="30"><use href="#icon-mail"/></svg></div>
    <div class="nav-tab nav-tab--active"><svg width="38" height="38"><use href="#icon-gear"/></svg></div>
  </header>

  <div class="field field--filled" style="left:46px;top:153px;width:427px;height:72px">Benny-ben Sato<span class="caret"></span></div>
  <div class="field" style="left:46px;top:235px;width:427px;height:71px">Email</div>
  <div class="field" style="left:46px;top:316px;width:117px;height:72px">Age</div>
  <div class="field" style="left:171px;top:316px;width:302px;height:72px">Sex<span class="chevron"></span></div>
  <div class="field" style="left:46px;top:398px;width:427px;height:71px">Height<span class="chevron"></span></div>
  <div class="field" style="left:46px;top:479px;width:427px;height:72px">Discovery Range<span class="chevron"></span></div>

  <div class="pics-label">Enter up to 5 pics</div>
  <div class="pic pic--photo" style="left:46px" role="img" aria-label="Uploaded profile photo"></div>
  <div class="pic" style="left:155px"><svg width="60" height="60"><use href="#icon-person"/></svg></div>
  <div class="pic" style="left:264px"><svg width="60" height="60"><use href="#icon-person"/></svg></div>
  <div class="pic" style="left:373px"><svg width="60" height="60"><use href="#icon-person"/></svg></div>

  <div class="field" style="left:46px;top:750px;width:427px;height:73px">Profession<span class="chevron"></span></div>

  <nav class="tab-bar">
    <div class="tab tab--active">Profile</div>
    <div class="tab">Security</div>
    <div class="tab">Legal</div>
  </nav>
</section>

</body>
</html>
```